Harrowgate Home Works Sales Flyer

We want a sales flyer that outlines our companies strengths with Kitchen & Bath Remodeling. We would like highlight those aspects while also showcasing our ability to do decks and home additions. We want financing packages to be a big part of the flyer.

Target Market(s)

Residential Customers

Requirements
Must have
• Financing options
Highlight Kitchen & bath remodeling
Less subtle is our decks and home additions
Nice to have
• Keep within our logo colors-we are looking for informative flyers that leave homeowners eager to call us after a meeting

```html
<!DOCTYPE html>
<html lang="en">
<head>
<meta charset="utf-8">
<title>Harrowgate Home Works – Kitchen &amp; Bath Remodeling Flyer</title>
<link href="https://fonts.googleapis.com/css2?family=Lato:wght@400;700&family=Oswald:wght@600&display=swap" rel="stylesheet">
<style>
  :root{
    --navy:#0b1628;
    --orange:#ef5a24;
    --orange-soft:#f49a6c;
    --orange-pale:#f8b894;
    --blue:#2470bb;
    --ink:#1d1d1f;
    --paper:#ffffff;
    --backdrop:#e9e9ea;
  }
  *{margin:0;padding:0;box-sizing:border-box}
  html,body{width:1200px;height:1200px;overflow:hidden;background:var(--backdrop)}
  .canvas{position:relative;width:1200px;height:1200px;overflow:hidden}
  .flyer{
    position:absolute;left:148px;top:20px;
    width:1385px;height:1777px;background:var(--paper);
    transform:scale(0.653);transform-origin:0 0;
    font-family:"Lato",sans-serif;color:var(--ink);overflow:hidden;
  }
  .abs{position:absolute}
  .brand-panel{left:0;top:0;width:658px;height:280px;background:var(--navy)}
  .brand-name{
    position:absolute;left:0;right:0;top:78px;text-align:center;
    color:var(--paper);font-family:"Lato",sans-serif;font-weight:700;
    font-size:46px;letter-spacing:4px;line-height:62px;text-transform:uppercase;
  }
  .photo{position:absolute}
  .photo-kitchen-main{left:688px;top:37px;width:657px;height:428px;
    background:linear-gradient(160deg,#eef0f1 0%,#c9c7c3 35%,#7a4a2c 60%,#e8e6e2 80%,#5a3422 100%)}
  .photo-bath-white{left:57px;top:1151px;width:415px;height:394px;
    background:linear-gradient(170deg,#f2f3f4 0%,#d9dbde 50%,#a9adb2 100%)}
  .photo-bath-grey{left:497px;top:1151px;width:415px;height:394px;
    background:linear-gradient(180deg,#7c7f83 0%,#55585c 55%,#2e3033 100%)}
  .photo-kitchen-white{left:927px;top:1151px;width:415px;height:394px;
    background:linear-gradient(165deg,#f6f6f4 0%,#e6e2dc 45%,#b0704a 70%,#f1f0ee 100%)}
  .accent{position:absolute}
  .accent-top{left:681px;top:398px;width:112px;height:107px;background:var(--orange-soft);opacity:.9}
  .accent-mid{left:754px;top:1097px;width:111px;height:108px;background:var(--orange-soft);opacity:.85}
  .accent-low{left:1231px;top:1505px;width:111px;height:107px;background:var(--orange-pale);opacity:.9}
  .headline{position:absolute;left:37px;font-family:"Oswald",sans-serif;font-weight:600;line-height:1;text-transform:uppercase;white-space:nowrap}
  .headline-top{top:292px;font-size:90px;color:var(--orange);letter-spacing:1.5px}
  .headline-main{top:372px;font-size:116px;color:var(--blue);letter-spacing:0}
  .intro{position:absolute;left:41px;top:500px;width:630px;font-size:24px;line-height:29px}
  .benefits{position:absolute;left:46px;top:702px;width:690px;list-style:none}
  .benefits li{position:relative;padding-left:40px;font-size:24px;line-height:29px}
  .benefits li svg{position:absolute;left:0;top:4px;width:32px;height:32px}
  .benefits strong{font-weight:700}
  .offer-backdrop{position:absolute;left:983px;top:643px;width:402px;height:395px;background:var(--navy)}
  .offer{position:absolute;left:843px;top:596px;width:404px;height:371px;background:var(--orange);color:var(--paper)}
  .offer-label{position:absolute;left:45px;top:42px;font-size:64px;line-height:1}
  .offer-value{position:absolute;left:62px;top:122px;font-size:138px;line-height:1}
  .offer-note{position:absolute;left:59px;top:266px;width:330px;font-size:22px;line-height:27px}
  .blue-band{position:absolute;left:0;top:1237px;width:705px;height:375px;background:var(--blue)}
  .closing{position:absolute;left:42px;top:1637px;width:640px;font-size:24px;line-height:29px}
  .contact-lead{position:absolute;left:844px;top:1630px;font-size:23px}
  .contact-phone{position:absolute;left:840px;top:1665px;display:flex;align-items:center;gap:14px;
    color:var(--blue);font-weight:700;font-size:54px;line-height:1}
  .contact-phone svg{width:46px;height:46px}
  .footer-bar{position:absolute;left:0;top:1735px;width:100%;height:42px;background:var(--orange)}
</style>
</head>
<body>
<div class="canvas">
  <article class="flyer">
    <header class="abs brand-panel">
      <div class="brand-name">Harrowgate<br>Home Works</div>
    </header>

    <div class="photo photo-kitchen-main" role="img" aria-label="Photo of a remodeled kitchen with walnut cabinets and a marble island"></div>
    <div class="accent accent-top"></div>

    <h1>
      <span class="headline headline-top">Kitchen &amp; Bath</span>
      <span class="headline headline-main">Remodeling</span>
    </h1>

    <p class="intro">From first sketch to final walkthrough, we design and build kitchens and bathrooms that fit the way your family lives. Custom cabinets, stone counters, tile showers and soaking tubs, all installed by our own licensed crews. We also build decks and home additions, so one trusted team handles every project on your list.</p>

    <ul class="benefits">
      <li style="margin-top:0"><svg viewBox="0 0 32 32"><circle cx="16" cy="16" r="13.5" fill="none" stroke="#2470bb" stroke-width="2"/><path d="M10 16.5l4.2 4.2L22 12" fill="none" stroke="#2470bb" stroke-width="2.4" stroke-linecap="round" stroke-linejoin="round"/></svg><strong>Financing packages:</strong> 0% interest for 18 months, or low fixed monthly payments up to 10 years, on approved credit.</li>
      <li style="margin-top:26px"><svg viewBox="0 0 32 32"><circle cx="16" cy="16" r="13.5" fill="none" stroke="#2470bb" stroke-width="2"/><path d="M10 16.5l4.2 4.2L22 12" fill="none" stroke="#2470bb" stroke-width="2.4" stroke-linecap="round" stroke-linejoin="round"/></svg>Full kitchen remodels with custom cabinets, islands, stone counters and new lighting</li>
      <li style="margin-top:40px"><svg viewBox="0 0 32 32"><circle cx="16" cy="16" r="13.5" fill="none" stroke="#2470bb" stroke-width="2"/><path d="M10 16.5l4.2 4.2L22 12" fill="none" stroke="#2470bb" stroke-width="2.4" stroke-linecap="round" stroke-linejoin="round"/></svg>Bathroom makeovers with walk-in showers and soaking tubs</li>
      <li style="margin-top:34px"><svg viewBox="0 0 32 32"><circle cx="16" cy="16" r="13.5" fill="none" stroke="#2470bb" stroke-width="2"/><path d="M10 16.5l4.2 4.2L22 12" fill="none" stroke="#2470bb" stroke-width="2.4" stroke-linecap="round" stroke-linejoin="round"/></svg>Custom decks and home additions, designed, permitted and built by the same crew</li>
      <li style="margin-top:31px"><svg viewBox="0 0 32 32"><circle cx="16" cy="16" r="13.5" fill="none" stroke="#2470bb" stroke-width="2"/><path d="M10 16.5l4.2 4.2L22 12" fill="none" stroke="#2470bb" stroke-width="2.4" stroke-linecap="round" stroke-linejoin="round"/></svg>Free in-home estimate and a written quote in 48 hours</li>
    </ul>

    <div class="offer-backdrop"></div>
    <section class="offer">
      <div class="offer-label">Financing</div>
      <div class="offer-value">0%</div>
      <p class="offer-note">Interest for 18 months on<br>approved credit. Ask us today!</p>
    </section>

    <div class="blue-band"></div>
    <div class="photo photo-bath-white" role="img" aria-label="Photo of a bright marble bathroom with a freestanding tub"></div>
    <div class="photo photo-bath-grey" role="img" aria-label="Photo of a grey paneled bathroom with double vessel sinks"></div>
    <div class="photo photo-kitchen-white" role="img" aria-label="Photo of a white kitchen island with wood shelving"></div>
    <div class="accent accent-mid"></div>
    <div class="accent accent-low"></div>

    <p class="closing">Ask about financing packages for kitchens, baths, decks and home additions, and book your free in-home estimate today.</p>

    <p class="contact-lead">For more details &amp; information please call us @</p>
    <div class="contact-phone">
      <svg viewBox="0 0 46 46"><circle cx="23" cy="23" r="20.5" fill="none" stroke="#ef5a24" stroke-width="2.5"/><path d="M16.5 12.5l4 0 2 5.5-2.6 2c1.3 2.8 3.3 4.8 6.1 6.1l2-2.6 5.5 2 0 4c0 1-1 2-2 2-9 0-17-8-17-17 0-1 1-2 2-2z" fill="#ef5a24"/></svg>
      <span>555 014 2678</span>
    </div>

    <div class="footer-bar"></div>
  </article>
</div>
</body>
</html>
```